Training flyer for 1/2 day modules

We need a flyer to be designed for some training sessions. It needs to be professional for the defence industry. It also needs to be able to be completed online - with tick boxes etc. Should be A4 back to back. Included in the documents below is some samples of previous brochures that we have had. Also below are some reviews from previous training - please use these somewhere;

- Great training, best I've ever had on this topic.
- Great presenter - very knowledgable.
- Course was very well presented and organised.

PLEASE USE MODULE TRAINING MOCK-UP FLYER ATTACHED FILE FOR CONTENT.

Target Market(s)

Defence industry

Industry/Entity Type

Defence

Requirements
Must have
• professional look - be able to be completed online,

```html
<!DOCTYPE html>
<html lang="en">
<head>
<meta charset="utf-8">
<title>Module Training – Half Day Sessions</title>
<link rel="stylesheet" href="https://fonts.googleapis.com/css2?family=Bebas+Neue&family=Oswald:wght@400;500&family=Lato:wght@400;700&display=swap">
<style>
  :root {
    --backdrop: #8d8d8d;
    --paper: #ffffff;
    --cyan: #1fb6e9;
    --green: #0d4d1f;
    --green-mid: #2f7d32;
    --grey-text: #666a6d;
    --ink: #2b2b2b;
    --row-grey: #e6e6e6;
    --bar-dark: #5b5b5b;
  }
  * { box-sizing: border-box; margin: 0; padding: 0; }
  html, body { width: 1200px; height: 900px; overflow: hidden; }
  body {
    background: radial-gradient(ellipse at center, #c9c9c9 0%, #9a9a9a 70%, var(--backdrop) 100%);
    font-family: "Lato", Arial, sans-serif;
    color: var(--ink);
    position: relative;
  }
  .page {
    position: absolute; top: 78px; height: 765px;
    background: var(--paper); overflow: hidden;
  }
  .page--front { left: 32px; width: 546px; }
  .page--back { left: 614px; width: 556px; }

  /* ---------- front ---------- */
  .hero-image {
    position: absolute; left: 0; top: 0; width: 546px; height: 280px;
    background: linear-gradient(160deg, #0a7fa8 0%, #35bde8 40%, #bfe9f8 60%, #2a9ccc 85%, #0e6f96 100%);
  }
  .hero-edge { position: absolute; left: 0; top: 230px; width: 546px; height: 60px; }
  .headline {
    position: absolute; left: 22px; font-family: "Bebas Neue", Impact, sans-serif;
    font-size: 80px; line-height: 1; white-space: nowrap;
    transform: scaleY(1.15); transform-origin: top left;
  }
  .headline--module { top: 268px; color: var(--cyan); letter-spacing: 3.4px; }
  .headline--training { top: 340px; color: var(--green); letter-spacing: 0; }
  .subhead {
    position: absolute; left: 22px; top: 421px; font-family: "Oswald", sans-serif;
    font-size: 18.5px; color: var(--grey-text); letter-spacing: 0.2px; line-height: 1; white-space: nowrap;
  }
  .schedule { position: absolute; left: 0; top: 467px; width: 238px; }
  .schedule__row {
    height: 19px; display: flex; align-items: center; padding: 0 8px 0 4px;
    font-family: "Oswald", sans-serif; font-size: 9.5px; color: #fff; white-space: nowrap;
  }
  .schedule__row:nth-child(odd) { background: var(--green); }
  .schedule__row:nth-child(even) { background: var(--cyan); }
  .schedule__dots { flex: 1; border-bottom: 1px dashed rgba(255,255,255,.7); margin: 0 3px; height: 1px; }
  .price {
    position: absolute; left: 22px; top: 539px; font-family: "Bebas Neue", Impact, sans-serif;
    font-size: 30px; color: var(--cyan); letter-spacing: 0.5px; line-height: 1; white-space: nowrap;
  }
  .team-photo {
    position: absolute; left: 0; top: 579px; width: 238px; height: 116px;
    background: linear-gradient(90deg, #d9d0c4 0%, #f1ede6 40%, #c8cfd8 75%, #9fb0c4 100%);
  }
  .footer-band { position: absolute; left: 0; top: 690px; width: 546px; height: 75px; }
  .front-contact {
    position: absolute; left: 24px; top: 712px; color: #fff; line-height: 1.35;
  }
  .front-contact__phone { font-size: 14px; }
  .front-contact__address { font-size: 10.5px; }
  .web-address {
    position: absolute; font-family: "Lato", sans-serif; font-size: 11.5px;
    letter-spacing: 2.6px; color: #fff;
  }
  .page--front .web-address { left: 273px; top: 736px; }

  .brand {
    position: absolute; display: flex; align-items: center; gap: 10px;
  }
  .brand__mark { width: 46px; height: 46px; border-radius: 50%; background: var(--green-mid); flex: none; }
  .brand__name {
    font-family: "Oswald", sans-serif; font-weight: 500; font-size: 19px; line-height: 1.05;
    color: var(--green); width: 130px;
  }
  .page--front .brand { left: 302px; top: 292px; }

  .modules { position: absolute; left: 273px; top: 382px; width: 253px; }
  .module { margin-bottom: 14px; }
  .module__title {
    font-family: "Bebas Neue", Impact, sans-serif; font-size: 14px; color: var(--green);
    letter-spacing: 0.2px; line-height: 1; margin-bottom: 1px; white-space: nowrap;
  }
  .module__body { font-size: 8.2px; line-height: 10.4px; text-align: justify; }

  /* ---------- back ---------- */
  .city-backdrop {
    position: absolute; inset: 0;
    background: linear-gradient(180deg, #d7e2e8 0%, #eef3f6 30%, #e4ecf0 60%, #c9d7de 85%, #bccbd2 100%);
  }
  .back-footer { position: absolute; left: 0; top: 632px; width: 556px; height: 133px; }
  .register {
    position: absolute; left: 18px; top: 22px; width: 512px;
    border: 1px solid #999; border-radius: 0 0 8px 8px; background: #fff; overflow: hidden;
  }
  .register__head {
    height: 26px; background: var(--cyan); color: #fff; font-weight: 700; font-size: 12.5px;
    display: flex; align-items: center; justify-content: space-between; padding: 0 64px 0 22px;
  }
  .register__cols {
    height: 23px; background: var(--bar-dark); display: grid;
    grid-template-columns: 328px 60px 67px 57px; color: #fff; font-size: 10px; font-weight: 700;
  }
  .register__cols span { display: flex; align-items: center; justify-content: center; }
  .register__row {
    display: grid; grid-template-columns: 328px 60px 67px 57px; height: 43px;
    border-top: 1px solid #aaa;
  }
  .register__row > div { border-left: 1px solid #aaa; display: flex; justify-content: center; padding-top: 12px; }
  .register__row > div:first-child { border-left: none; background: var(--row-grey); display: block; padding: 12px 14px 0 22px; }
  .register__row > div:nth-child(3) { background: var(--row-grey); }
  .field { display: flex; align-items: flex-end; font-size: 9.5px; line-height: 13px; }
  .field__line { flex: 1; border-bottom: 1px solid #666; margin-left: 4px; margin-bottom: 3px; }
  .tick-box { width: 7px; height: 7px; border: 1px solid #444; display: inline-block; background: #fff; }

  .panel {
    position: absolute; left: 18px; width: 512px; background: #e8e8e8;
    border: 1px solid #999; border-radius: 8px; padding: 10px 20px 0 22px;
  }
  .panel .field { margin-bottom: 5px; }
  .panel--company { top: 262px; height: 76px; }
  .panel--card { top: 377px; height: 153px; }
  .panel--card .field--gap { margin-top: 18px; }
  .payment {
    position: absolute; left: 40px; top: 351px; width: 470px; display: flex;
    font-size: 10px; align-items: center;
  }
  .payment__label { font-weight: 700; flex: 1; }
  .payment__option { margin-left: 34px; display: flex; align-items: center; gap: 5px; }
  .page--back .brand { left: 186px; top: 556px; }
  .back-contact {
    position: absolute; left: 0; width: 556px; top: 694px; text-align: center;
    color: #fff; line-height: 1.35;
  }
  .back-contact__phone { font-size: 12px; }
  .back-contact__address { font-size: 11px; }
  .page--back .web-address { left: 0; width: 556px; text-align: center; top: 730px; }
</style>
</head>
<body>

<section class="page page--front">
  <div class="hero-image" role="img" aria-label="Upward view of glass office towers against a blue sky"></div>
  <svg class="hero-edge" viewBox="0 0 546 60" preserveAspectRatio="none" aria-hidden="true">
    <path d="M0 22 L40 30 L70 18 L110 36 L150 26 L190 44 L230 30 L260 40 L300 24 L340 34 L380 20 L420 30 L470 16 L510 24 L546 12 L546 60 L0 60 Z" fill="#ffffff"/>
  </svg>

  <div class="headline headline--module">MODULE</div>
  <div class="headline headline--training">TRAINING</div>
  <div class="subhead">HALF DAY TRAINING SESSIONS</div>

  <div class="schedule">
    <div class="schedule__row"><span>SYDNEY</span><span class="schedule__dots"></span><span>27 &amp; 28 APRIL</span></div>
    <div class="schedule__row"><span>CANBERRA</span><span class="schedule__dots"></span><span>29 APRIL (MODULES 1 AND 2 ONLY)</span></div>
    <div class="schedule__row"><span>BRISBANE</span><span class="schedule__dots"></span><span>2 &amp; 3 MAY</span></div>
  </div>

  <div class="price">PRICE:&nbsp; $495 (INC GST)</div>
  <div class="team-photo" role="img" aria-label="Photograph of smiling business professionals in a meeting"></div>

  <svg class="footer-band" viewBox="0 0 546 75" preserveAspectRatio="none" aria-hidden="true">
    <polygon points="0,0 250,0 272,22 546,22 546,75 0,75" fill="var(--green)"/>
  </svg>
  <div class="front-contact">
    <div class="front-contact__phone">Phone: 61 (0)7 5550 0148</div>
    <div class="front-contact__address">Level 2, 14 Harbour Lane, Seaview</div>
  </div>
  <div class="web-address">http://tradeready-training.example/</div>

  <div class="brand">
    <span class="brand__mark"></span>
    <span class="brand__name">Northgate Trade Compliance</span>
  </div>

  <div class="modules">
    <article class="module">
      <h2 class="module__title">1. Australian Export Controls and AU/US Trade Treaty</h2>
      <p class="module__body">This half day module provides attendees with guidance on Australian Export Controls and the recent changes and provide guidance on management of the new requirements. Included in this session is information with regard to the Trade Co-operation Treaty.</p>
    </article>
    <article class="module">
      <h2 class="module__title">2.&nbsp; Jurisdiction/Classification</h2>
      <p class="module__body">This half day module will take attendees through export control reform and provide practical step by step guidance on Jurisdiction and Classification of U.S. controlled technology. Attendees will be encouraged to bring their own examples to be worked through during the training session.</p>
    </article>
    <article class="module">
      <h2 class="module__title">3.&nbsp; Dual Nationals, Discrimination and Privacy</h2>
      <p class="module__body">The contradiction between the U.S. Dual National Requirements and Australian Anti-Discrimination has long been an issue for the Australian defence industry. Further compounding the issues is the new Australian Privacy Legislation. This module provides attendees with guidance on how to manage the issue and tip and hints on mitigation strategies.</p>
    </article>
    <article class="module">
      <h2 class="module__title">4.&nbsp; Exemptions, Exceptions &amp; De Minimis</h2>
      <p class="module__body">Exemptions, Exceptions and De-minimis primarily allows exporters to export U.S. controlled technology without prior approval, however, there are restrictions. This module will explore Exemptions, Exceptions and De-minimis and provide practical guidance on implementation and management.</p>
    </article>
  </div>
</section>

<section class="page page--back">
  <div class="city-backdrop" role="img" aria-label="Faint city skyline in pale blue-grey tones"></div>

  <div class="register">
    <div class="register__head"><span>HOW TO REGISTER</span><span>LOCATION</span></div>
    <div class="register__cols"><span></span><span>Sydney</span><span>Canberra</span><span>Brisbane</span></div>
    <div class="register__row">
      <div><div class="field">Attendee name:<span class="field__line"></span></div><div class="field">Email:<span class="field__line"></span></div></div>
      <div><span class="tick-box"></span></div><div><span class="tick-box"></span></div><div><span class="tick-box"></span></div>
    </div>
    <div class="register__row">
      <div><div class="field">Attendee name:<span class="field__line"></span></div><div class="field">Email:<span class="field__line"></span></div></div>
      <div><span class="tick-box"></span></div><div><span class="tick-box"></span></div><div><span class="tick-box"></span></div>
    </div>
    <div class="register__row">
      <div><div class="field">Attendee name:<span class="field__line"></span></div><div class="field">Email:<span class="field__line"></span></div></div>
      <div><span class="tick-box"></span></div><div><span class="tick-box"></span></div><div><span class="tick-box"></span></div>
    </div>
    <div class="register__row">
      <div><div class="field">Attendee name:<span class="field__line"></span></div><div class="field">Email:<span class="field__line"></span></div></div>
      <div><span class="tick-box"></span></div><div><span class="tick-box"></span></div><div><span class="tick-box"></span></div>
    </div>
  </div>

  <div class="panel panel--company">
    <div class="field">Company:<span class="field__line"></span></div>
    <div class="field">Email:<span class="field__line"></span></div>
    <div class="field">Phone:<span class="field__line"></span></div>
  </div>

  <div class="payment">
    <span class="payment__label">PAYMENT METHOD:</span>
    <span class="payment__option">Invoice <span class="tick-box"></span></span>
    <span class="payment__option">Credit card <span class="tick-box"></span></span>
  </div>

  <div class="panel panel--card">
    <div class="field">Credit card number:<span class="field__line"></span></div>
    <div class="field">Card name:<span class="field__line"></span></div>
    <div class="field">Expiry date:<span class="field__line"></span></div>
    <div class="field">CVV:<span class="field__line"></span></div>
    <div class="field">Card holder email:<span class="field__line"></span></div>
    <div class="field field--gap">Email:<span class="field__line"></span></div>
  </div>

  <div class="brand">
    <span class="brand__mark"></span>
    <span class="brand__name">Northgate Trade Compliance</span>
  </div>

  <svg class="back-footer" viewBox="0 0 556 133" preserveAspectRatio="none" aria-hidden="true">
    <path d="M0 40 L30 28 L60 38 L95 20 L130 34 L170 14 L210 30 L250 8 L290 26 L330 12 L370 30 L410 16 L450 32 L490 18 L525 30 L556 22 L556 133 L0 133 Z" fill="var(--green)"/>
  </svg>
  <div class="back-contact">
    <div class="back-contact__phone">Phone: 61 (0)7 5550 0148</div>
    <div class="back-contact__address">Level 2, 14 Harbour Lane, Seaview</div>
  </div>
  <div class="web-address">http://tradeready-training.example/</div>
</section>

</body>
</html>
```